Web Page Color Scheme

I need the colors chosen for all of the elements in a B2B web application page (screenshot attached).

We have a web application that serves businesses (not consumers), generally Corvane 300 companies. The pages are fully developed/functional. What I want is to improve the look and feel so that the page has a more premium feel. That is the entire goal, to make the pages have a very premium feel to them. I don’t know if it is the best analogy but if you think of Varn or Pallisene as average and KTR or Osprin as premium, we want users to get a very premium feel the first time they see the screens.

What I am looking for right now is just colors. Below I describe the details.

#1 Improve the colors

The color scheme is blue and yellow. Black, gray and white are also used. I do not think the base colors should change (that is, I think we will continue to use blue and yellow) but I do think which hues, shades, tints or tones of blue, yellow and gray we use could benefit from some improvement. Feel free to use any blues, yellows and grays you think look best, lighter or darker colors, etc. You can also feel free to change what colors are used where. One note, aqua blue does not look premium. It might be deco looking or otherwise good for some things but I don’t think you will see an aqua colored Hollaway driving down the street any time soon.

Quill products tend to have a premium feel but I don’t think I am looking for a stark white appearance.

I want every color defined including but not necessarily limited to:

Backgrounds

Page Header
Navigation Panel
Page Body
Table Header
Table Header Button (the Add button)
Table Column Header
Table Rows (maybe alternating, maybe not)
Checkboxes
Table Footer

Not all of these have to be different. I assume some will be the same. I just need each carefully
thought through.

Fonts

Page Header
Navigation Panel
Page Title
Table Header Title
Table Header Button
Table Column Header
Table Row
Table Footer

Icons

Page Header
Navigation Panel
Table expander/collapse
Actions
Table Footer

Target Market(s)

Corvane 300/Pinnacle 1200

Requirements
Must have
• Premium feel

```html
<!DOCTYPE html>
<html lang="en">
<head>
<meta charset="utf-8">
<title>Data Sources</title>
<link href="https://fonts.googleapis.com/css2?family=Roboto:wght@400;500;700&display=swap" rel="stylesheet">
<style>
:root{
  --header-bg:#0e1729;
  --header-text:#eef1f6;
  --nav-top:#17233b;
  --nav-bottom:#1d2d4c;
  --nav-text:#d9deea;
  --nav-sub:#b7bfd1;
  --gold:#c9a43a;
  --gold-soft:#dcbc5a;
  --gold-ink:#2a2210;
  --page-bg:#f3f2ee;
  --panel-bg:#ffffff;
  --band:#1f3863;
  --band-text:#f4f1e6;
  --col-head:#131f38;
  --col-head-text:#e9ecf3;
  --row-bg:#ffffff;
  --row-alt:#f8f7f3;
  --foot-bg:#eeece6;
  --line:#dedbd2;
  --text:#2a2f3a;
  --muted:#6b7080;
  --title:#15223d;
  --ico:#2b3b5e;
  --ico-edit:#a9852a;
  --rule-a:#dbe1f2;
  --rule-b:#f4e4ab;
  --rule-d:#ecd3ce;
  --rule-e:#cde4d3;
  --check-on:#2b3b5e;
}
*{box-sizing:border-box;margin:0;padding:0}
html,body{width:1200px;height:1053px;overflow:hidden}
body{font-family:"Roboto",sans-serif;font-size:13px;color:var(--text);background:var(--page-bg);position:relative}
.topbar{position:absolute;left:0;top:0;width:1200px;height:71px;background:var(--header-bg);color:var(--header-text);border-bottom:2px solid var(--gold)}
.brand{position:absolute;left:18px;top:20px;display:flex;align-items:center;gap:39px;font-size:27px;font-weight:400}
.brand-dot{width:30px;height:30px;border-radius:50%;background:var(--gold)}
.menu-toggle{position:absolute;left:272px;top:30px}
.tools{position:absolute;left:962px;top:26px;display:flex;gap:12px}
.user{position:absolute;left:1103px;top:31px;font-size:13px;font-weight:500;display:flex;gap:8px;align-items:center}
.sidebar{position:absolute;left:0;top:71px;width:242px;height:982px;overflow:hidden;color:var(--nav-text)}
.sidebar svg.bg{position:absolute;left:0;top:0}
.nav{position:relative;list-style:none;padding-top:14px}
.nav li{height:36px;display:flex;align-items:center;font-size:13px;gap:10px;padding-left:18px}
.nav li.sub{padding-left:66px;color:var(--nav-sub)}
.nav li.sub-ico{padding-left:34px;color:var(--nav-sub)}
.nav li.active{color:var(--gold-soft)}
.badge{margin-left:16px;background:var(--gold);color:var(--gold-ink);font-weight:500;font-size:15px;width:33px;height:24px;border-radius:12px;display:flex;align-items:center;justify-content:center}
.nav-foot{position:absolute;left:72px;top:943px;font-size:13px;letter-spacing:.6px;color:#e8ebf2}
.page-title{position:absolute;left:257px;top:86px;font-size:24px;font-weight:500;color:var(--title)}
.search{position:absolute;left:934px;top:86px;width:243px;height:27px;border:1px solid #cbc8bf;background:#fff;display:flex}
.search span{margin-left:auto;width:31px;border-left:1px solid #cbc8bf;background:#e9e7e0;display:flex;align-items:center;justify-content:center}
.panel{position:absolute;left:257px;top:128px;width:920px;border:1px solid var(--line);background:var(--panel-bg)}
.band{background:var(--band);color:var(--band-text);display:flex;align-items:center;gap:10px;font-size:16px;padding-left:10px}
.add{background:var(--gold);color:var(--gold-ink);font-size:13px;padding:1px 6px;border-radius:2px}
table{border-collapse:collapse;table-layout:fixed;width:100%}
th{background:var(--col-head);color:var(--col-head-text);font-weight:700;font-size:13px;text-align:left;height:28px;padding-left:6px;border-right:1px solid #2d3a55}
th.c{text-align:center;padding-left:0}
td{height:28px;border:1px solid var(--line);padding-left:6px;white-space:nowrap;background:var(--row-bg)}
.sources > tbody > tr:nth-child(even) > td:not(.nest),.fields tr:nth-child(odd) td{background:var(--row-alt)}
td.x{width:20px;padding:0;text-align:center;border-right:none}
.exp{width:12px;height:12px;vertical-align:middle}
.acts{display:flex;gap:14px;justify-content:center}
.acts svg{width:16px;height:16px}
.nest{padding:0 0 0 20px;border:none;background:var(--page-bg)}
.nest-box{border:1px solid var(--line);border-right:none;background:#fff}
.cnt{position:absolute;right:16px;color:var(--muted)}
.pk{display:inline-block;width:15px;height:15px;border:1px solid #d3d0c7;border-radius:3px;background:#fff;vertical-align:middle}
.pk.on{background:var(--check-on);border-color:var(--check-on)}
.rules{display:flex;gap:6px;padding-left:6px}
.r{width:24px;height:22px;display:flex;align-items:center;justify-content:center;font-size:14px;font-weight:700;color:var(--ico);border-radius:2px}
.r svg{width:16px;height:16px}
.r.a{background:var(--rule-a)}.r.b{background:var(--rule-b)}.r.d{background:var(--rule-d)}.r.e{background:var(--rule-e)}
.r.c{outline:2px solid var(--ico);outline-offset:-3px;border-radius:3px}
.foot{height:29px;display:flex;align-items:center;padding-left:16px;gap:6px;position:relative;color:var(--muted);background:var(--foot-bg);border-top:1px solid var(--line)}
.per{border:1px solid #cbc8bf;background:#fff;width:52px;height:18px;padding-left:3px;font-size:12px;display:flex;align-items:center;justify-content:space-between;padding-right:4px}
.pager{position:absolute;left:400px;display:flex;gap:16px;align-items:center;color:#a9adb8;font-size:11px}
.pager b{background:var(--gold);color:var(--gold-ink);font-weight:500;font-size:13px;width:21px;height:20px;display:flex;align-items:center;justify-content:center}
</style>
</head>
<body>
<svg width="0" height="0" style="position:absolute">
  <defs>
    <symbol id="i-exp" viewBox="0 0 12 12"><circle cx="6" cy="6" r="6" fill="#1f3863"/><path d="M5 3.5 7.5 6 5 8.5" stroke="#fff" stroke-width="1.6" fill="none"/></symbol>
    <symbol id="i-col" viewBox="0 0 12 12"><circle cx="6" cy="6" r="6" fill="#1f3863"/><path d="M3.5 5 6 7.5 8.5 5" stroke="#fff" stroke-width="1.6" fill="none"/></symbol>
    <symbol id="i-bolt" viewBox="0 0 16 16"><path d="M9 1 4 9h4l-1 6 5-8H8z" fill="#2b3b5e"/></symbol>
    <symbol id="i-edit" viewBox="0 0 16 16"><rect x="1.5" y="3" width="11" height="11" rx="1.5" fill="none" stroke="#2b3b5e" stroke-width="1.4"/><path d="M6 10l1-3 6-6 2 2-6 6z" fill="#2b3b5e"/></symbol>
    <symbol id="i-copy" viewBox="0 0 16 16"><rect x="1.5" y="5" width="9" height="10" rx="1" fill="none" stroke="#2b3b5e" stroke-width="1.4"/><rect x="5.5" y="1" width="9" height="10" rx="1" fill="#fff" stroke="#2b3b5e" stroke-width="1.4"/></symbol>
    <symbol id="i-trash" viewBox="0 0 16 16"><rect x="2" y="2" width="12" height="2" fill="#2b3b5e"/><rect x="6" y="0.5" width="4" height="2" fill="#2b3b5e"/><path d="M3.5 5h9l-1 10h-7z" fill="#2b3b5e"/><path d="M6.5 7v6M9.5 7v6" stroke="#fff" stroke-width="1"/></symbol>
    <symbol id="i-edit-gold" viewBox="0 0 16 16"><rect x="1.5" y="3" width="11" height="11" rx="1.5" fill="none" stroke="#2b3b5e" stroke-width="1.4"/><path d="M6 10l1-3 6-6 2 2-6 6z" fill="#a9852a"/></symbol>
    <symbol id="i-search" viewBox="0 0 16 16"><circle cx="7" cy="6" r="4" fill="none" stroke="#2b3b5e" stroke-width="2"/><path d="M10 9l4 5" stroke="#2b3b5e" stroke-width="2.5"/></symbol>
    <symbol id="i-dup" viewBox="0 0 16 16"><rect x="2" y="5" width="9" height="9" fill="none" stroke="#2b3b5e" stroke-width="1.6"/><path d="M5 5V2h9v9h-3" fill="none" stroke="#2b3b5e" stroke-width="1.6"/></symbol>
    <symbol id="i-fork" viewBox="0 0 16 16"><circle cx="3" cy="3" r="2" fill="#2b3b5e"/><circle cx="13" cy="3" r="2" fill="#2b3b5e"/><path d="M3 3c0 5 5 4 5 8v4M13 3c0 5-5 4-5 8" stroke="#2b3b5e" stroke-width="1.8" fill="none"/></symbol>
    <symbol id="i-target" viewBox="0 0 16 16"><circle cx="8" cy="8" r="6" fill="none" stroke="#2b3b5e" stroke-width="1.6"/><circle cx="8" cy="8" r="2" fill="#2b3b5e"/><path d="M8 0v4M8 12v4M0 8h4M12 8h4" stroke="#2b3b5e" stroke-width="1.6"/></symbol>
    <symbol id="i-list" viewBox="0 0 16 16"><rect x="1" y="2" width="14" height="2.4" fill="#2b3b5e"/><rect x="5" y="6" width="10" height="2" fill="#2b3b5e"/><rect x="5" y="9.5" width="10" height="2" fill="#2b3b5e"/><rect x="1" y="13" width="14" height="2" fill="#2b3b5e"/><path d="M1 6l3 2.7-3 2.7z" fill="#2b3b5e"/></symbol>
  </defs>
</svg>

<header class="topbar">
  <div class="brand"><span class="brand-dot"></span>Acme Data</div>
  <svg class="menu-toggle" width="14" height="12" viewBox="0 0 14 12"><path d="M0 1h14M0 6h14M0 11h14" stroke="#eef1f6" stroke-width="2.2"/></svg>
  <div class="tools">
    <svg width="22" height="20" viewBox="0 0 22 20"><path d="M2 16a9 9 0 0 1 18 0" fill="none" stroke="#eef1f6" stroke-width="2"/><path d="M11 16l4-7" stroke="#eef1f6" stroke-width="2"/></svg>
    <svg width="22" height="20" viewBox="0 0 22 20"><path d="M2 19 14 7" stroke="#eef1f6" stroke-width="2.6"/><path d="M16 1v4M14 3h4M20 8v3M18.5 9.5h3M9 2v3M7.5 3.5h3" stroke="#dcbc5a" stroke-width="1.4"/></svg>
    <svg width="20" height="20" viewBox="0 0 20 20"><circle cx="10" cy="10" r="10" fill="#eef1f6"/><text x="10" y="15" text-anchor="middle" font-family="Roboto,sans-serif" font-weight="700" font-size="14" fill="#0e1729">?</text></svg>
    <svg width="20" height="20" viewBox="0 0 20 20"><circle cx="10" cy="10" r="6.5" fill="none" stroke="#eef1f6" stroke-width="5" stroke-dasharray="3 2.1"/><circle cx="10" cy="10" r="6" fill="#eef1f6"/><circle cx="10" cy="10" r="2.5" fill="#0e1729"/></svg>
  </div>
  <div class="user">Fred Fixit <svg width="10" height="6" viewBox="0 0 10 6"><path d="M0 0h10L5 6z" fill="#eef1f6"/></svg></div>
</header>

<nav class="sidebar">
  <svg class="bg" width="242" height="982" viewBox="0 0 242 982" role="img" aria-label="Soft deep blue wave background">
    <defs>
      <linearGradient id="g-nav" x1="0" y1="0" x2="0" y2="1"><stop offset="0" stop-color="#17233b"/><stop offset="1" stop-color="#1d2d4c"/></linearGradient>
      <linearGradient id="g-wave" x1="0" y1="0" x2="0" y2="1"><stop offset="0" stop-color="#2a4677"/><stop offset="1" stop-color="#3a5f9e"/></linearGradient>
    </defs>
    <rect width="242" height="982" fill="url(#g-nav)"/>
    <path d="M120 600C170 540 210 545 242 535V982H120z" fill="#24375d" opacity=".8"/>
    <path d="M0 460C50 520 70 720 170 770C200 782 225 780 242 778V982H0z" fill="url(#g-wave)"/>
  </svg>
  <ul class="nav">
    <li><svg width="16" height="14" viewBox="0 0 16 14"><circle cx="5" cy="4" r="3" fill="#d9deea"/><circle cx="11" cy="4" r="3" fill="#d9deea"/><path d="M0 13c0-5 10-5 10 0zM8 13c0-4 8-5 8 0z" fill="#d9deea"/></svg>Users</li>
    <li class="sub">Roles</li>
    <li class="sub">Notification Groups<span class="badge">9</span></li>
    <li class="active"><svg width="14" height="14" viewBox="0 0 14 14"><ellipse cx="7" cy="3" rx="6" ry="2.5" fill="#dcbc5a"/><path d="M1 5c0 3 12 3 12 0v3c0 3-12 3-12 0zM1 10c0 3 12 3 12 0v1.5c0 3-12 3-12 0z" fill="#dcbc5a"/></svg>Data Sources</li>
    <li class="sub-ico"><svg width="16" height="12" viewBox="0 0 16 12"><rect x="1" y="4" width="4" height="4" fill="none" stroke="#b7bfd1"/><rect x="11" y="1" width="4" height="4" fill="none" stroke="#b7bfd1"/><rect x="11" y="7" width="4" height="4" fill="none" stroke="#b7bfd1"/><path d="M5 6h3M8 3v6M8 3h3M8 9h3" stroke="#b7bfd1"/></svg>Data Object Relationships</li>
    <li><svg width="16" height="12" viewBox="0 0 16 12"><path d="M0 1h16M0 6h16M0 11h16M5 0v12" stroke="#d9deea" stroke-width="1.2"/></svg>Data Sets</li>
    <li><svg width="16" height="14" viewBox="0 0 16 14"><path d="M0 1h3M5 1h11M0 5h3M5 5h11M0 9h3M5 9h11M0 13h3M5 13h11" stroke="#d9deea" stroke-width="1.6"/></svg>Rule Sets</li>
    <li><svg width="16" height="16" viewBox="0 0 16 16"><circle cx="8" cy="8" r="6.5" fill="none" stroke="#d9deea" stroke-width="1.4"/><path d="M8 4v4l3 2" stroke="#d9deea" stroke-width="1.4" fill="none"/></svg>Schedules</li>
    <li><svg width="18" height="14" viewBox="0 0 18 14"><path d="M2 5h12l-3-3M16 9H4l3 3" stroke="#d9deea" stroke-width="2.2" fill="none"/></svg>Metadata Import/Export</li>
    <li class="sub">Import</li>
    <li class="sub">Export</li>
  </ul>
  <div class="nav-foot">ACME DATA</div>
</nav>

<h1 class="page-title">Data Sources</h1>
<div class="search"><span><svg width="12" height="12" viewBox="0 0 12 12"><circle cx="5" cy="5" r="3.6" fill="none" stroke="#2b3b5e" stroke-width="1.6"/><path d="M8 8l3 3" stroke="#2b3b5e" stroke-width="1.8"/></svg></span></div>

<section class="panel">
  <div class="band" style="height:34px">Data Sources <span class="add">Add</span></div>
  <table>
    <colgroup><col style="width:272px"><col style="width:253px"><col style="width:253px"><col></colgroup>
    <tr><th style="padding-left:25px">Data Source Name ▲</th><th>Type ⇕</th><th>Status ⇕</th><th class="c">Actions</th></tr>
  </table>
  <table class="sources">
    <colgroup><col style="width:20px"><col style="width:252px"><col style="width:253px"><col style="width:253px"><col></colgroup>
    <tbody>
    <tr><td class="x"><svg class="exp"><use href="#i-exp"/></svg></td><td style="border-left:none">relbase</td><td></td><td>Active</td><td><div class="acts"><svg><use href="#i-bolt"/></svg><svg><use href="#i-edit"/></svg><svg><use href="#i-copy"/></svg><svg><use href="#i-trash"/></svg></div></td></tr>
    <tr><td class="x"><svg class="exp"><use href="#i-exp"/></svg></td><td style="border-left:none">Skyforce - Sanbox</td><td>Skyforce.io</td><td>Active</td><td><div class="acts"><svg><use href="#i-bolt"/></svg><svg><use href="#i-edit"/></svg><svg><use href="#i-copy"/></svg><svg><use href="#i-trash"/></svg></div></td></tr>
    <tr><td class="x"><svg class="exp"><use href="#i-exp"/></svg></td><td style="border-left:none">SKFC</td><td>Skyforce.io</td><td>Active</td><td><div class="acts"><svg><use href="#i-bolt"/></svg><svg><use href="#i-edit"/></svg><svg><use href="#i-copy"/></svg><svg><use href="#i-trash"/></svg></div></td></tr>
    <tr><td class="x"><svg class="exp"><use href="#i-col"/></svg></td><td style="border-left:none">skfc 44</td><td>Skyforce.io</td><td>Active</td><td><div class="acts"><svg><use href="#i-bolt"/></svg><svg><use href="#i-edit"/></svg><svg><use href="#i-copy"/></svg><svg><use href="#i-trash"/></svg></div></td></tr>
    <tr><td colspan="5" class="nest">
      <div class="nest-box">
        <div class="band" style="height:36px">Data Objects <span class="add">Add</span></div>
        <table>
          <colgroup><col style="width:20px"><col><col style="width:68px"></colgroup>
          <tr><th colspan="2" style="padding-left:25px">Data Object Name</th><th class="c">Actions</th></tr>
          <tr><td class="x"><svg class="exp"><use href="#i-col"/></svg></td><td style="border-left:none;padding-left:12px;position:relative">Account<span class="cnt">28 fields</span></td><td style="text-align:center;padding:0"><svg width="16" height="16"><use href="#i-trash"/></svg></td></tr>
          <tr><td colspan="3" class="nest" style="padding-right:0">
            <div class="nest-box" style="border-bottom:none">
              <div class="band" style="height:35px">Fields <span class="add">Add</span></div>
              <table class="fields">
                <colgroup><col style="width:255px"><col style="width:255px"><col style="width:100px"><col style="width:200px"><col></colgroup>
                <tr><th>Field Name</th><th>Data Type</th><th class="c">Primary Key</th><th class="c">Rule Types</th><th class="c">Actions</th></tr>
                <tr><td>Id</td><td>Common.ID</td><td style="text-align:center"><span class="pk on"></span></td><td><div class="rules"><span class="r">a✓</span><span class="r"><svg><use href="#i-search"/></svg></span><span class="r"><svg><use href="#i-dup"/></svg></span><span class="r"><svg><use href="#i-fork"/></svg></span><span class="r"><svg><use href="#i-target"/></svg></span><span class="r"><svg><use href="#i-list"/></svg></span></div></td><td><div class="acts"><svg><use href="#i-edit-gold"/></svg><svg><use href="#i-trash"/></svg></div></td></tr>
                <tr><td>Name</td><td>Organization.Name</td><td style="text-align:center"><span class="pk"></span></td><td><div class="rules"><span class="r a">a✓</span><span class="r b"><svg><use href="#i-search"/></svg></span><span class="r c"><svg><use href="#i-dup"/></svg></span><span class="r d"><svg><use href="#i-fork"/></svg></span><span class="r e"><svg><use href="#i-target"/></svg></span><span class="r e"><svg><use href="#i-list"/></svg></span></div></td><td><div class="acts"><svg><use href="#i-edit-gold"/></svg><svg><use href="#i-trash"/></svg></div></td></tr>
                <tr><td>Phone</td><td>Phone.Phone Number</td><td style="text-align:center"><span class="pk"></span></td><td><div class="rules"><span class="r a">a✓</span><span class="r b"><svg><use href="#i-search"/></svg></span><span class="r c"><svg><use href="#i-dup"/></svg></span><span class="r d"><svg><use href="#i-fork"/></svg></span><span class="r e"><svg><use href="#i-target"/></svg></span><span class="r e"><svg><use href="#i-list"/></svg></span></div></td><td><div class="acts"><svg><use href="#i-edit-gold"/></svg><svg><use href="#i-trash"/></svg></div></td></tr>
                <tr><td>Type</td><td>Address.Address Line 1</td><td style="text-align:center"><span class="pk"></span></td><td><div class="rules"><span class="r a">a✓</span><span class="r b"><svg><use href="#i-search"/></svg></span><span class="r c"><svg><use href="#i-dup"/></svg></span><span class="r d"><svg><use href="#i-fork"/></svg></span><span class="r e"><svg><use href="#i-target"/></svg></span><span class="r e"><svg><use href="#i-list"/></svg></span></div></td><td><div class="acts"><svg><use href="#i-edit-gold"/></svg><svg><use href="#i-trash"/></svg></div></td></tr>
                <tr><td>BillingCity</td><td>Address.City</td><td style="text-align:center"><span class="pk"></span></td><td><div class="rules"><span class="r a">a✓</span><span class="r b"><svg><use href="#i-search"/></svg></span><span class="r c"><svg><use href="#i-dup"/></svg></span><span class="r d"><svg><use href="#i-fork"/></svg></span><span class="r e"><svg><use href="#i-target"/></svg></span><span class="r e"><svg><use href="#i-list"/></svg></span></div></td><td><div class="acts"><svg><use href="#i-edit-gold"/></svg><svg><use href="#i-trash"/></svg></div></td></tr>
                <tr><td>BillingCountry</td><td>Address.Country</td><td style="text-align:center"><span class="pk"></span></td><td><div class="rules"><span class="r a">a✓</span><span class="r b"><svg><use href="#i-search"/></svg></span><span class="r c"><svg><use href="#i-dup"/></svg></span><span class="r d"><svg><use href="#i-fork"/></svg></span><span class="r e"><svg><use href="#i-target"/></svg></span><span class="r e"><svg><use href="#i-list"/></svg></span></div></td><td><div class="acts"><svg><use href="#i-edit-gold"/></svg><svg><use href="#i-trash"/></svg></div></td></tr>
                <tr><td>BillingLatitude</td><td>Geographic.Latitude</td><td style="text-align:center"><span class="pk"></span></td><td><div class="rules"><span class="r a">a✓</span><span class="r"><svg><use href="#i-search"/></svg></span><span class="r c"><svg><use href="#i-dup"/></svg></span><span class="r"><svg><use href="#i-fork"/></svg></span><span class="r e"><svg><use href="#i-target"/></svg></span><span class="r e"><svg><use href="#i-list"/></svg></span></div></td><td><div class="acts"><svg><use href="#i-edit-gold"/></svg><svg><use href="#i-trash"/></svg></div></td></tr>
                <tr><td>BillingLongitude</td><td>Geographic.Longitude</td><td style="text-align:center"><span class="pk"></span></td><td><div class="rules"><span class="r a">a✓</span><span class="r"><svg><use href="#i-search"/></svg></span><span class="r c"><svg><use href="#i-dup"/></svg></span><span class="r"><svg><use href="#i-fork"/></svg></span><span class="r e"><svg><use href="#i-target"/></svg></span><span class="r e"><svg><use href="#i-list"/></svg></span></div></td><td><div class="acts"><svg><use href="#i-edit-gold"/></svg><svg><use href="#i-trash"/></svg></div></td></tr>
                <tr><td>BillingState</td><td>Address.State or Province</td><td style="text-align:center"><span class="pk"></span></td><td><div class="rules"><span class="r a">a✓</span><span class="r"><svg><use href="#i-search"/></svg></span><span class="r c"><svg><use href="#i-dup"/></svg></span><span class="r"><svg><use href="#i-fork"/></svg></span><span class="r e"><svg><use href="#i-target"/></svg></span><span class="r e"><svg><use href="#i-list"/></svg></span></div></td><td><div class="acts"><svg><use href="#i-edit-gold"/></svg><svg><use href="#i-trash"/></svg></div></td></tr>
                <tr><td>BillingStreet</td><td>Address.Address Line 1</td><td style="text-align:center"><span class="pk"></span></td><td><div class="rules"><span class="r a">a✓</span><span class="r"><svg><use href="#i-search"/></svg></span><span class="r c"><svg><use href="#i-dup"/></svg></span><span class="r"><svg><use href="#i-fork"/></svg></span><span class="r e"><svg><use href="#i-target"/></svg></span><span class="r e"><svg><use href="#i-list"/></svg></span></div></td><td><div class="acts"><svg><use href="#i-edit-gold"/></svg><svg><use href="#i-trash"/></svg></div></td></tr>
                <tr><td>BillingPostalCode</td><td>Address.ZIP or Postal Code</td><td style="text-align:center"><span class="pk"></span></td><td><div class="rules"><span class="r a">a✓</span><span class="r"><svg><use href="#i-search"/></svg></span><span class="r c"><svg><use href="#i-dup"/></svg></span><span class="r"><svg><use href="#i-fork"/></svg></span><span class="r e"><svg><use href="#i-target"/></svg></span><span class="r e"><svg><use href="#i-list"/></svg></span></div></td><td><div class="acts"><svg><use href="#i-edit-gold"/></svg><svg><use href="#i-trash"/></svg></div></td></tr>
                <tr><td>LastModifiedDate</td><td>Common.Last Updated Date</td><td style="text-align:center"><span class="pk"></span></td><td><div class="rules"><span class="r">a✓</span><span class="r"><svg><use href="#i-search"/></svg></span><span class="r"><svg><use href="#i-dup"/></svg></span><span class="r"><svg><use href="#i-fork"/></svg></span><span class="r e"><svg><use href="#i-target"/></svg></span><span class="r e"><svg><use href="#i-list"/></svg></span></div></td><td><div class="acts"><svg><use href="#i-edit-gold"/></svg><svg><use href="#i-trash"/></svg></div></td></tr>
                <tr><td>Website</td><td>Organization.Website/URL</td><td style="text-align:center"><span class="pk"></span></td><td><div class="rules"><span class="r a">a✓</span><span class="r"><svg><use href="#i-search"/></svg></span><span class="r c"><svg><use href="#i-dup"/></svg></span><span class="r"><svg><use href="#i-fork"/></svg></span><span class="r e"><svg><use href="#i-target"/></svg></span><span class="r e"><svg><use href="#i-list"/></svg></span></div></td><td><div class="acts"><svg><use href="#i-edit-gold"/></svg><svg><use href="#i-trash"/></svg></div></td></tr>
              </table>
            </div>
          </td></tr>
          <tr><td class="x"><svg class="exp"><use href="#i-exp"/></svg></td><td style="border-left:none;padding-left:12px;position:relative">Contact<span class="cnt">26 fields</span></td><td style="text-align:center;padding:0"><svg width="16" height="16"><use href="#i-trash"/></svg></td></tr>
          <tr><td class="x"><svg class="exp"><use href="#i-exp"/></svg></td><td style="border-left:none;padding-left:12px;position:relative">Lead<span class="cnt">17 fields</span></td><td style="text-align:center;padding:0"><svg width="16" height="16"><use href="#i-trash"/></svg></td></tr>
        </table>
      </div>
    </td></tr>
    <tr><td class="x"><svg class="exp"><use href="#i-exp"/></svg></td><td style="border-left:none">skfc 99</td><td>Skyforce.io</td><td>Active</td><td><div class="acts"><svg><use href="#i-bolt"/></svg><svg><use href="#i-edit"/></svg><svg><use href="#i-copy"/></svg><svg><use href="#i-trash"/></svg></div></td></tr>
    <tr><td class="x"><svg class="exp"><use href="#i-exp"/></svg></td><td style="border-left:none">SKFC - Field Entry Test</td><td>Skyforce.io</td><td>Active</td><td><div class="acts"><svg><use href="#i-bolt"/></svg><svg><use href="#i-edit"/></svg><svg><use href="#i-copy"/></svg><svg><use href="#i-trash"/></svg></div></td></tr>
    </tbody>
  </table>
  <div class="foot">6 of 6 records <span class="per">20 <svg width="10" height="6" viewBox="0 0 10 6"><path d="M1 1l4 4 4-4" stroke="#6b7080" stroke-width="1.5" fill="none"/></svg></span>
    <div class="pager"><span>◀◀</span><span>◀</span><b>1</b><span>▶</span><span>▶▶</span></div>
  </div>
</section>
</body>
</html>
```